WTR PDAK Thank You card

We need a thank you card to give to our various stakeholders. The card design needs to be professional, corporate, and use elements of our current visual identity (colours and logo will be supplied). The inside of the card needs to have a space for a personal message to be written. Our target card size is 5 x 7.

As a bit of background, we fund local health care in Northvale. We do not directly provide front-line health care services. We do manage the funding and performance monitoring for the agencies we fund. We engage a wide range of people from CEO's, to MPP's, to the general public on a variety of health care topics. At the heart of it, we are a local organization that works to improve health care in Windsor/Essex, Chatham-Kent, and Sarnia/Lambton.

The final design should lean towards a more traditional look.

• It must incorporate our colour pallet and logo

```html
<!DOCTYPE html>
<html lang="en">
<head>
<meta charset="utf-8">
<title>WTR PDAK Thank You Card</title>
<link rel="stylesheet" href="https://fonts.googleapis.com/css2?family=Great+Vibes&family=Open+Sans:wght@400;600&display=swap">
<style>
  :root {
    --page: #e6e6e6;
    --card: #ffffff;
    --gold: #c4b888;
    --gold-script: #bfae6e;
    --script-shadow: #3b3422;
    --ink: #111111;
    --card-shadow: rgba(0,0,0,0.18);
  }
  * { margin: 0; padding: 0; box-sizing: border-box; }
  html, body {
    width: 900px; height: 1200px; overflow: hidden;
    background: var(--page);
    font-family: "Open Sans", Arial, sans-serif;
  }
  .sheet { position: relative; width: 900px; height: 1200px; }
  .card-face {
    position: absolute; left: 90px; width: 720px; height: 500px;
    background: var(--card);
    box-shadow: 0 4px 14px var(--card-shadow);
    overflow: hidden;
  }
  .card-face--front { top: 60px; }
  .card-face--back { top: 640px; }
  .pattern-band {
    position: absolute; left: 0; top: 0; width: 100%; height: 178px;
    background: linear-gradient(180deg, #c9bd8e 0%, #c1b483 100%);
  }
  .accent-rule {
    position: absolute; left: 0; top: 189px; width: 100%; height: 14px;
    background: var(--gold);
  }
  .thank-you {
    position: absolute; left: 0; right: 0; top: 265px;
    text-align: center;
    font-family: "Great Vibes", cursive;
    font-size: 108px; line-height: 1;
    color: var(--gold-script);
    text-shadow: 2px 3px 0 var(--script-shadow);
  }
  .signature-mark {
    position: absolute; right: 40px; bottom: 30px;
    display: flex; align-items: center; gap: 8px;
    font-size: 24px; font-weight: 600; color: var(--ink);
  }
  .mark-square { width: 20px; height: 20px; background: var(--ink); }
  .identity-block {
    position: absolute; left: 190px; top: 262px; width: 300px;
    color: var(--ink);
  }
  .identity-name {
    display: flex; align-items: center; gap: 12px;
    font-size: 40px; font-weight: 600; line-height: 1;
    padding-bottom: 6px;
    border-bottom: 2px solid var(--ink);
  }
  .identity-name .mark-square { width: 30px; height: 30px; }
  .identity-line {
    margin-left: 72px;
    font-size: 13px; font-weight: 600; line-height: 1.3;
  }
  .identity-line--en { padding: 5px 0 4px; border-bottom: 1px solid var(--ink); }
  .identity-line--fr { padding-top: 4px; }
</style>
</head>
<body>
<main class="sheet">
  <section class="card-face card-face--front" aria-label="Card front">
    <div class="pattern-band" role="img" aria-label="Repeating leaf pattern band in muted gold"></div>
    <div class="accent-rule"></div>
    <h1 class="thank-you">Thank you!</h1>
    <div class="signature-mark">
      <span class="mark-square"></span>
      <span>Northvale</span>
    </div>
  </section>

  <section class="card-face card-face--back" aria-label="Card back">
    <div class="pattern-band" role="img" aria-label="Repeating leaf pattern band in muted gold"></div>
    <div class="accent-rule"></div>
    <div class="identity-block">
      <div class="identity-name">
        <span class="mark-square"></span>
        <span>Northvale</span>
      </div>
      <p class="identity-line identity-line--en">WTR PDAK Westerly Regional<br>Health Partnership Network</p>
      <p class="identity-line identity-line--fr">Réseau régional de partenariat<br>des services de santé<br>de Westerly</p>
    </div>
  </section>
</main>
</body>
</html>
```